Website update for Harbor Broker Ledger & Payroll Services

Our website needs updating
www.harborbrokerledgers.com
Here are some of our latest print pieces to use as a guide?
I have also attached our graphic identity guide which includes the Pantone colors

Target Market(s)

Insurance Agencies

Industry/Entity Type

Accounting

Number of Pages Required

5+ page

```html
<!DOCTYPE html>
<html lang="en">
<head>
<meta charset="utf-8">
<title>Harbor Broker Ledger & Payroll Services</title>
<link href="https://fonts.googleapis.com/css2?family=Open+Sans:wght@400;600;700;800&display=swap" rel="stylesheet">
<style>
:root{
  --teal:#22a99a;
  --teal-dark:#1a8f83;
  --ink:#333a3f;
  --muted:#6b7377;
  --light:#f1f3f3;
  --line:#dde2e2;
  --white:#ffffff;
  --overlay:rgba(38,44,48,.86);
  --footer:#f7f8f8;
}
*{box-sizing:border-box;margin:0;padding:0}
html,body{width:820px;height:1200px;overflow:hidden;background:var(--white)}
body{font-family:"Open Sans",Arial,sans-serif;color:var(--ink);position:relative}
.topbar{height:18px;background:var(--teal);display:flex;justify-content:flex-end;align-items:center;gap:14px;padding:0 82px;font-size:8px;color:var(--white)}
.site-header{height:58px;display:flex;align-items:center;justify-content:space-between;padding:0 82px}
.brand{display:flex;align-items:center;gap:7px}
.brand-mark{width:22px;height:22px;background:var(--teal)}
.brand-name{font-weight:700;font-size:10.5px;line-height:1.15;color:var(--teal);width:120px}
.main-nav{display:flex;gap:2px}
.main-nav a{font-size:8px;font-weight:600;color:var(--ink);text-decoration:none;padding:6px 6px;letter-spacing:.2px}
.main-nav a.active{background:var(--teal);color:var(--white)}
.hero{position:absolute;top:104px;left:0;width:820px;height:282px;background:linear-gradient(100deg,#e8ecec 0%,#cfd6d5 35%,#b9c2c1 60%,#8f9a9c 100%)}
.hero-card{position:absolute;left:490px;top:70px;width:212px;height:118px;background:var(--overlay);padding:18px 16px}
.hero-title{color:var(--teal);font-weight:800;font-size:13px;line-height:1.2;letter-spacing:.3px}
.hero-text{color:var(--white);font-size:9px;line-height:1.45;margin-top:8px;font-weight:600}
.hero-dots{position:absolute;left:675px;top:195px;display:flex;gap:4px}
.hero-dots span{width:5px;height:5px;border-radius:50%;background:var(--white)}
.hero-dots span.on{background:var(--teal)}
.services{position:absolute;top:445px;left:82px;width:656px}
.section-title{text-align:center;font-weight:800;font-size:20px;color:var(--ink);letter-spacing:.5px}
.section-rule{width:30px;height:2px;background:var(--teal);margin:8px auto 0}
.service-row{display:flex;gap:26px;margin-top:30px}
.service{flex:1}
.service-head{display:flex;align-items:center;gap:10px;height:40px}
.service-icon{flex:0 0 36px;height:36px;border-radius:50%;background:var(--teal);display:flex;align-items:center;justify-content:center}
.service-name{font-weight:700;font-size:11px;line-height:1.25;color:var(--ink)}
.service-desc{font-size:8px;line-height:1.6;color:var(--muted);margin-top:14px}
.about{position:absolute;top:705px;left:0;width:820px;height:235px;background:var(--light)}
.about-photo{position:absolute;left:0;top:0;width:405px;height:235px;background:linear-gradient(120deg,#dfe4e3 0%,#c4cdcc 45%,#a9b3b2 100%)}
.about-copy{position:absolute;left:420px;top:20px;width:320px}
.about-title{font-weight:700;font-size:14px;line-height:1.3;color:var(--ink)}
.about-lead{font-weight:700;font-size:9.5px;line-height:1.4;color:var(--teal);margin-top:10px}
.about-list{list-style:none;margin-top:8px}
.about-list li{font-size:7.5px;line-height:1.5;color:var(--ink);padding-left:10px;position:relative;margin-bottom:2px}
.about-list li::before{content:"";position:absolute;left:0;top:4px;width:4px;height:4px;border-radius:50%;background:var(--teal)}
.about-sub{font-weight:700;font-size:9.5px;color:var(--teal);margin-top:8px}
.site-footer{position:absolute;top:940px;left:0;width:820px;height:230px;background:var(--footer);border-top:1px solid var(--line);padding:26px 82px;display:flex;gap:40px}
.footer-col h4{font-size:9.5px;font-weight:700;color:var(--ink);margin-bottom:8px}
.footer-col h4::after{content:"";display:block;width:22px;height:2px;background:var(--teal);margin-top:5px}
.quick-links{width:130px}
.quick-links a{display:block;font-size:8px;line-height:1.65;color:var(--muted);text-decoration:none}
.contact{width:190px;font-size:8px;line-height:1.65;color:var(--muted)}
.contact p+p{margin-top:8px}
.signup{width:220px}
.signup-form{display:flex;margin-top:2px}
.signup-input{width:150px;height:22px;border:1px solid var(--line);background:var(--white);font-size:7.5px;color:#9aa1a4;padding:0 6px;display:flex;align-items:center}
.signup-btn{height:22px;padding:0 9px;background:var(--teal);color:var(--white);font-size:7.5px;font-weight:700;display:flex;align-items:center}
.connect{margin-top:18px}
.social{display:flex;gap:6px}
.social span{width:20px;height:20px;border-radius:50%;background:var(--teal)}
.copyright{position:absolute;left:0;top:1170px;width:820px;height:30px;background:var(--ink);color:#c9cfd1;font-size:7px;display:flex;align-items:center;padding:0 82px;letter-spacing:.3px}
</style>
</head>
<body>
<div class="topbar">
  <span>hello@harborbrokerledgers.com</span>
  <span>|</span>
  <span>(555) 014-7260</span>
</div>
<header class="site-header">
  <div class="brand">
    <span class="brand-mark"></span>
    <span class="brand-name">Harbor Broker Ledger &amp; Payroll</span>
  </div>
  <nav class="main-nav">
    <a class="active" href="#">HOME</a>
    <a href="#">ABOUT US</a>
    <a href="#">COMPARE</a>
    <a href="#">OUR SERVICES</a>
    <a href="#">HOW IT WORKS</a>
    <a href="#">RESOURCES</a>
    <a href="#">CONTACT US</a>
    <a href="#">BLOG</a>
  </nav>
</header>

<section class="hero" role="img" aria-label="Photo of smiling clients meeting with an accounting advisor">
  <div class="hero-card">
    <h1 class="hero-title">INSURANCE AGENCY ACCOUNTANTS</h1>
    <p class="hero-text">Specialists in providing accounting support services to independent Insurance Agencies</p>
  </div>
  <div class="hero-dots"><span class="on"></span><span></span><span></span></div>
</section>

<section class="services">
  <h2 class="section-title">OUR SERVICES</h2>
  <div class="section-rule"></div>
  <div class="service-row">
    <article class="service">
      <div class="service-head">
        <span class="service-icon">
          <svg width="16" height="16" viewBox="0 0 16 16"><path d="M4 1h6l3 3v11H4z" fill="none" stroke="#fff" stroke-width="1.5"/><path d="M6 7h5M6 10h5" stroke="#fff" stroke-width="1.3"/></svg>
        </span>
        <h3 class="service-name">Record Direct Bill</h3>
      </div>
      <p class="service-desc">We post every direct bill commission statement promptly, match it to your policies and flag any variance so your producers are always paid correctly.</p>
    </article>
    <article class="service">
      <div class="service-head">
        <span class="service-icon">
          <svg width="16" height="16" viewBox="0 0 16 16"><circle cx="8" cy="8" r="6.5" fill="none" stroke="#fff" stroke-width="1.5"/><path d="M10 5.5H7a1.25 1.25 0 0 0 0 2.5h2a1.25 1.25 0 0 1 0 2.5H6M8 4v1.5M8 10.5V12" fill="none" stroke="#fff" stroke-width="1.2"/></svg>
        </span>
        <h3 class="service-name">Reconcile &amp; Pay Agency Bill Premiums</h3>
      </div>
      <p class="service-desc">Agency bill invoices are reconciled against carrier statements each month, and premium payments are scheduled on time to keep your carrier relationships strong.</p>
    </article>
    <article class="service">
      <div class="service-head">
        <span class="service-icon">
          <svg width="16" height="16" viewBox="0 0 16 16"><rect x="2" y="2" width="12" height="12" fill="none" stroke="#fff" stroke-width="1.5"/><path d="M2 6h12M6 6v8" stroke="#fff" stroke-width="1.2"/></svg>
        </span>
        <h3 class="service-name">Reconcile General Ledger Accounts</h3>
      </div>
      <p class="service-desc">Bank, trust and operating accounts are balanced against your ledger, giving you clean monthly financials and a clear view of agency performance.</p>
    </article>
  </div>
</section>

<section class="about">
  <div class="about-photo" role="img" aria-label="Photo of business people shaking hands across a desk"></div>
  <div class="about-copy">
    <h2 class="about-title">Experienced team of insurance agency bookkeeping professionals maintaining your books</h2>
    <p class="about-lead">Affordable, professional services for less than the cost of an in-house bookkeeper</p>
    <ul class="about-list">
      <li>Pay-as-you-grow model that scales with your agency</li>
      <li>No backlogs or costly rework of past entries</li>
      <li>Regular updates of financial status and reports</li>
    </ul>
    <p class="about-sub">Capabilities</p>
    <ul class="about-list">
      <li>Services from basic bookkeeping to financial analysis</li>
      <li>Specialists in leading agency management systems</li>
      <li>Trusted by agency owners, managers and staff</li>
    </ul>
  </div>
</section>

<footer class="site-footer">
  <div class="footer-col quick-links">
    <h4>Quick Links</h4>
    <a href="#">Home</a>
    <a href="#">About Us</a>
    <a href="#">Compare</a>
    <a href="#">Our Services</a>
    <a href="#">How It Works</a>
    <a href="#">Resources</a>
    <a href="#">Contact Us</a>
    <a href="#">Blog</a>
  </div>
  <div class="footer-col contact">
    <h4>Contact Us</h4>
    <p>Harbor Broker Ledger &amp; Payroll Services<br>482 Wharf Row Road<br>Portside, CT 06000</p>
    <p>Phone (555) 014-7260<br>Fax (555) 014-7261<br>Email contact us</p>
  </div>
  <div class="footer-col signup">
    <h4>Sign Up For Our Email List</h4>
    <div class="signup-form">
      <span class="signup-input">Enter your email address</span>
      <span class="signup-btn">SUBSCRIBE</span>
    </div>
    <div class="connect">
      <h4>Connect With Us</h4>
      <div class="social"><span></span><span></span><span></span><span></span></div>
    </div>
  </div>
</footer>
<div class="copyright">COPYRIGHT © 2024 HARBOR BROKER LEDGER &amp; PAYROLL SERVICES. ALL RIGHTS RESERVED.</div>
</body>
</html>
```